Business Card Design Project for a Restaurant/Wine Bar

New, fresh business card design for Verdano Wine Bar & Restaurant, Saltmere, Calvera. We are an established restaurant on the Calvera coast featuring "Italian coastal cuisine."

"Verdano" means bay leaf in Italian. We aren't sure if we would like our logo on the card or not, but if you have something interesting that uses it, then please do so. The basic information is essential - full restaurant name, address, phone and website (do not use www). The font on our menu and wine list may give you some sort of an idea of our style.

One-sided card needed as we often use the backside to write down various types of info for customers.

After seeing a few submissions, we would like to see what designers can come up with-using the logo, just the leaf, or none at all. Sky is the limit as long as our full restaurant name, address, phone and website (please leave out www) are there. Please contact us if questions!

I appreciate all of your designs! Our deadline is next week, but I will continue to give feedback on designs as I can. This is our busiest season, so my co-owner/chef/husband, won't have time to look at the designs for awhile. When he does, we can make our decision.

cheers,
Mirel

Target Market(s)

Fine dining/wine crowd. Would like something simple and elegant, but not pretentious or stuffy. Verdano means bay laurel (bay leaf) in Italian (please see our logo).

Industry/Entity Type

Restaurant

Requirements
Must have
• Full Name of Restaurant: Verdano Wine Bar & Restaurant
Address: 812 Fenwick Ave NW, Saltmere, Calvera 97538
Phone: 541.555.0193
website: verdanowinebar.example (do not use www)
Should not have
• Loud colors.

```html
<!DOCTYPE html>
<html lang="en">
<head>
<meta charset="utf-8">
<title>Verdano Wine Bar &amp; Restaurant — Business Card</title>
<link rel="stylesheet" href="https://fonts.googleapis.com/css2?family=Libre+Baskerville:wght@400;700&display=swap">
<style>
  :root {
    --backdrop: #d8d4cb;
    --card: #dfe3d6;
    --brown: #4a2c17;
    --rust: #c0733e;
    --shadow: rgba(40, 28, 15, 0.25);
  }
  * { box-sizing: border-box; margin: 0; padding: 0; }
  html, body {
    width: 1200px;
    height: 1023px;
    overflow: hidden;
    background: var(--backdrop);
  }
  .canvas {
    width: 1200px;
    height: 1023px;
    display: flex;
    align-items: center;
    justify-content: center;
  }
  .card {
    width: 520px;
    height: 910px;
    background: var(--card);
    box-shadow: 0 10px 30px var(--shadow);
    display: flex;
    flex-direction: column;
    align-items: center;
    padding: 100px 40px 0;
    font-family: "Libre Baskerville", Georgia, serif;
    color: var(--brown);
    text-align: center;
  }
  .wordmark {
    font-size: 76px;
    font-weight: 400;
    letter-spacing: 0.04em;
    line-height: 1;
    color: var(--brown);
  }
  .brand-name {
    margin-top: 130px;
    font-size: 28px;
    font-weight: 700;
    letter-spacing: 0.08em;
    text-transform: uppercase;
  }
  .brand-tagline {
    margin-top: 6px;
    font-size: 20px;
    font-variant: small-caps;
    letter-spacing: 0.06em;
    color: var(--rust);
  }
  .contact { margin-top: 28px; }
  .contact-label {
    font-size: 15px;
    font-weight: 700;
    letter-spacing: 0.1em;
    text-transform: uppercase;
    color: var(--rust);
    margin-top: 18px;
  }
  .contact-value {
    font-size: 26px;
    line-height: 1.3;
    color: var(--brown);
  }
</style>
</head>
<body>
<main class="canvas">
  <article class="card">
    <div class="wordmark">Verdano</div>

    <h1 class="brand-name">Verdano</h1>
    <p class="brand-tagline">Wine Bar &amp; Restaurant</p>

    <section class="contact">
      <p class="contact-label">Address</p>
      <p class="contact-value">812 Fenwick Ave NW, Saltmere,<br>Calvera 97538</p>

      <p class="contact-label">Phone</p>
      <p class="contact-value">541.555.0193</p>

      <p class="contact-label">Website</p>
      <p class="contact-value">verdanowinebar.example</p>
    </section>
  </article>
</main>
</body>
</html>
```